Tilda Tinkerwire, An IT Company Has New Logo, Need Fresh Business Cards

IT company is called Tilda Tinkerwire and is displayed nicely with the new logo from here on pitchloft. Would like a fresh business card look that encompasses the idea that we want clients to Cherish Every Gadget. I love the use of circuitry with hearts as endpoints and x's and o's. It needs to have room for my certification logos of which there are 4 and a BRJ Alumni log. I am attaching my current card to illustrate how it has always captured attention, but that was in the early stages of business when I was doing more residential work. I am focused on businesses now, so a level of professionalism is necessary. I would also like the card to lend itself well to additional stationary, email signature, ticketing template for my workboard, etc. For the time being, I need the card for an upcoming conference so that work will come later. Color scheme should be that of the new logo. Thank you and I look forward to the designs.

Target Market(s)

Businesses looking for IT services.

Industry/Entity Type

Information Technology

Contact Information for Business Card

See above

Requirements
Must have
• New logo colors and a warm feel. Possibly a tad feminine as I am female, but appealing to males.
Nice to have
• I would like techy, but no too much so. I like friendly and connecting feels. People LOVED my old card and called me because it gave them a warm feeling.

```html
<!DOCTYPE html>
<html lang="en">
<head>
<meta charset="utf-8">
<title>Tilda Tinkerwire – Business Card</title>
<link rel="stylesheet" href="https://fonts.googleapis.com/css2?family=Lato:wght@400;700&display=swap">
<style>
  :root {
    --stage: #1c1c1c;
    --card-front: #f2f2f2;
    --card-back: #81c9e9;
    --card-back-deep: #74bfe2;
    --accent-blue: #6bbfe6;
    --accent-pink: #d59ad0;
    --accent-green: #c9dc7c;
    --ink: #111111;
    --white: #ffffff;
    --badge-gold: #b39a5f;
    --badge-grey: #c9ccd1;
    --badge-blue: #9fd2ee;
  }
  * { box-sizing: border-box; margin: 0; padding: 0; }
  html, body {
    width: 1200px; height: 900px; overflow: hidden;
    background: var(--stage);
    font-family: "Lato", Arial, sans-serif;
  }
  .stage { position: relative; width: 1200px; height: 900px; }
  .card {
    position: absolute; top: 170px;
    width: 347px; height: 561px; overflow: hidden;
  }
  .card--front { left: 259px; background: var(--card-front); text-align: center; }
  .card--back { left: 631px; background: var(--card-back); color: var(--white); text-align: center; }

  /* front */
  .brand-mark {
    position: absolute; top: 262px; left: 0; width: 100%;
    display: flex; justify-content: center; align-items: center; gap: 10px;
    transform: translateY(-100px);
  }
  .brand-mark__dot { width: 18px; height: 18px; border-radius: 50%; border: 3px solid var(--accent-pink); }
  .brand-mark__name { font-size: 24px; font-weight: 700; color: var(--accent-blue); }
  .person { position: absolute; top: 239px; width: 100%; }
  .person__name { font-size: 20px; font-weight: 700; color: var(--accent-blue); letter-spacing: 0.5px; }
  .person__role { font-size: 15px; color: var(--ink); margin-top: 3px; }
  .contact-icons {
    position: absolute; top: 300px; width: 100%;
    display: flex; justify-content: center; gap: 5px;
  }
  .contact { position: absolute; top: 320px; width: 100%; font-size: 15.5px; color: var(--ink); line-height: 20.5px; }

  .badges { position: absolute; top: 418px; left: 0; width: 100%; }
  .badge-row { display: flex; justify-content: center; gap: 12px; margin-bottom: 22px; }
  .badge { height: 44px; border-radius: 4px; }
  .badge--alumni { width: 72px; background: var(--badge-gold); }
  .badge--cert { width: 78px; background: var(--badge-grey); border-bottom: 4px solid var(--badge-blue); }
  .badge--partner { width: 94px; background: var(--badge-grey); border-bottom: 4px solid var(--badge-blue); }
  .badge--tech { width: 120px; background: var(--badge-grey); border-bottom: 4px solid var(--badge-blue); }

  /* back */
  .back-texture {
    position: absolute; inset: 0;
    background: radial-gradient(circle at 50% 40%, var(--card-back) 0%, var(--card-back-deep) 100%);
  }
  .back-brand { position: absolute; top: 316px; width: 100%; }
  .back-brand__row { display: flex; justify-content: center; align-items: center; gap: 10px; }
  .back-brand__dot { width: 16px; height: 16px; border-radius: 50%; background: var(--white); }
  .back-brand__name { font-size: 29px; font-weight: 400; letter-spacing: -0.3px; }
  .back-brand__tagline { font-size: 10.5px; letter-spacing: 3px; text-transform: uppercase; margin-top: 2px; }
  .services {
    position: absolute; top: 492px; width: 100%;
    display: flex; justify-content: center; gap: 14px;
    font-size: 17.5px; list-style: none;
  }
  .services li { display: flex; align-items: center; gap: 11px; }
  .services li::before {
    content: ""; width: 9px; height: 9px; border-radius: 50%; background: var(--white);
  }
</style>
</head>
<body>
<main class="stage">

  <section class="card card--front" aria-label="Card front">
    <div class="brand-mark">
      <span class="brand-mark__dot"></span>
      <span class="brand-mark__name">Tilda Tinkerwire</span>
    </div>

    <div class="person">
      <h1 class="person__name">TILDA</h1>
      <p class="person__role">Director</p>
    </div>

    <div class="contact-icons" aria-hidden="true">
      <svg width="13" height="13" viewBox="0 0 24 24"><path fill="#6bbfe6" d="M6.6 10.8a15.1 15.1 0 0 0 6.6 6.6l2.2-2.2c.3-.3.7-.4 1-.2 1.1.4 2.3.6 3.6.6.6 0 1 .4 1 1V20c0 .6-.4 1-1 1A17 17 0 0 1 3 4c0-.6.4-1 1-1h3.5c.6 0 1 .4 1 1 0 1.3.2 2.5.6 3.6.1.3 0 .7-.2 1z"/></svg>
      <svg width="13" height="13" viewBox="0 0 24 24"><rect x="2" y="5" width="20" height="14" rx="1" fill="#6bbfe6"/><path d="M2 6l10 7 10-7" stroke="#f2f2f2" stroke-width="1.8" fill="none"/></svg>
      <svg width="13" height="13" viewBox="0 0 24 24"><circle cx="12" cy="12" r="10" fill="#6bbfe6"/><path d="M2 12h20M12 2c3 3 3 17 0 20M12 2c-3 3-3 17 0 20" stroke="#f2f2f2" stroke-width="1.3" fill="none"/></svg>
    </div>

    <address class="contact" style="font-style:normal">
      <p>407-555-0188</p>
      <p>hello@tildatinkerwire.com</p>
      <p>www.tilda-tinkerwire.com</p>
    </address>

    <div class="badges" aria-label="Alumni and certification badges">
      <div class="badge-row">
        <span class="badge badge--alumni" role="img" aria-label="BRJ Alumni badge"></span>
        <span class="badge badge--cert" role="img" aria-label="Certification badge"></span>
        <span class="badge badge--partner" role="img" aria-label="Partner certification badge"></span>
      </div>
      <div class="badge-row">
        <span class="badge badge--cert" role="img" aria-label="Professional certification badge"></span>
        <span class="badge badge--tech" role="img" aria-label="Technician certification badge"></span>
      </div>
    </div>
  </section>

  <section class="card card--back" aria-label="Card back">
    <div class="back-texture" role="img" aria-label="Faint circuit line pattern in light blue"></div>

    <div class="back-brand">
      <div class="back-brand__row">
        <span class="back-brand__dot"></span>
        <span class="back-brand__name">Tilda Tinkerwire</span>
      </div>
      <p class="back-brand__tagline">Cherish Every Gadget</p>
    </div>

    <ul class="services">
      <li>Desktops</li>
      <li>Laptops</li>
      <li>Tablets</li>
    </ul>
  </section>

</main>
</body>
</html>
```